Brisk Meadow

Hello,
I require the following to be completed for my business.
My company font is Spicy Rice, and I'm enclosing a picture of a logo.
Please amend the enclosed brochure to make it look better.(meadowbrochure6)
Please amend the enclosed installation guide, so it says my company name, addresses logo, etc on it (installation instructions).
Please create a letter head and business cards
My name is Tobin Varemchuk and my title is National Sales Manager, company address is on the site: briskmeadow.ca, tobin@briskmeadow.ca cell phone is 416-552-0918, I'm thinking we have just the logo on one side and "Premium Synthetic Turf" in spicy font. On the letter head, on the bottom i'm thinking of showing grass come up, see my website.
The BM_ Label pages is required to create product labels, please add a colourmark of my company logo in the designs. (I'll require 6 or 8 per page, and more product are coming, let's just iron down layout. (my sites product page has more products)
Target Market(s)
The target market will be home owners.
Industry/Entity Type
Cell Phone
Logo Text
Design Build Innovate
Look and feel
Each slider illustrates characteristics of the customer's brand and the style your logo design should communicate.

```html
<!DOCTYPE html>
<html lang="en">
<head>
<meta charset="utf-8">
<title>Brisk Meadow – Business Card Options</title>
<link href="https://fonts.googleapis.com/css2?family=Arimo:ital,wght@0,400;0,700;1,700&display=swap" rel="stylesheet">
<style>
  :root {
    --board-light: #f2f2f2;
    --board-dark: #4a4746;
    --card-white: #ffffff;
    --card-edge: #2e2e2e;
    --ink: #1c1c1c;
    --ink-light: #ffffff;
    --brand-green: #5c9a2c;
    --grass-deep: #3f8e1a;
    --grass-mid: #5fb52a;
    --grass-bright: #8fd14a;
    --grass-pale: #c6e89a;
    --sky-top: #4b9fe0;
    --sky-low: #d8ecfa;
    --bar-black: #0d0d0d;
  }
  html, body {
    margin: 0;
    padding: 0;
    width: 1200px;
    height: 1139px;
    overflow: hidden;
  }
  body {
    position: relative;
    background: radial-gradient(ellipse at 50% 48%, var(--board-light) 0%, #bdbdbd 45%, var(--board-dark) 100%);
    font-family: "Arimo", Arial, sans-serif;
  }
  .card {
    position: absolute;
    width: 519px;
    height: 298px;
    background: var(--card-white);
    outline: 1px solid var(--card-edge);
    overflow: hidden;
  }
  .card--r1c1 { left: 51px;  top: 45px; }
  .card--r1c2 { left: 645px; top: 46px; }
  .card--r2c1 { left: 51px;  top: 431px; }
  .card--r2c2 { left: 645px; top: 431px; }
  .card--r3c1 { left: 53px;  top: 794px; }
  .card--r3c2 { left: 645px; top: 794px; }

  .card__scene {
    position: absolute;
    inset: 0;
    width: 519px;
    height: 298px;
  }
  .card__name {
    position: absolute;
    left: 16px;
    top: 12px;
    margin: 0;
    font-size: 23px;
    font-weight: 400;
    color: var(--ink);
  }
  .card__title {
    position: absolute;
    left: 20px;
    top: 43px;
    margin: 0;
    font-size: 14px;
    font-weight: 700;
    font-style: italic;
    color: var(--ink);
  }
  .card__brand {
    position: absolute;
    left: 220px;
    top: 58px;
    width: 280px;
    margin: 0;
    text-align: center;
    font-size: 32px;
    font-weight: 700;
    line-height: 1;
    color: var(--brand-green);
  }
  .card__tagline {
    position: absolute;
    left: 220px;
    top: 101px;
    width: 280px;
    margin: 0;
    text-align: center;
    font-size: 16px;
    font-weight: 700;
    color: var(--brand-green);
  }
  .card__company {
    position: absolute;
    left: 12px;
    top: 207px;
    margin: 0;
    font-size: 19px;
    font-weight: 700;
    color: var(--ink-light);
  }
  .card__address {
    position: absolute;
    left: 13px;
    top: 233px;
    margin: 0;
    font-size: 16px;
    font-weight: 700;
    color: var(--ink-light);
  }
  .card__email, .card__phone {
    position: absolute;
    top: 268px;
    margin: 0;
    font-size: 16px;
    font-weight: 700;
    color: var(--ink-light);
  }
  .card__email { left: 16px; }
  .card__phone { right: 13px; }
  .card__company, .card__address, .card__email, .card__phone {
    text-shadow: 0 1px 2px rgba(0,0,0,0.35);
  }

  .card--sky .card__name,
  .card--sky .card__title { color: var(--ink-light); }
  .card--sky .card__tagline { color: var(--ink); }

  .card--slant .card__company,
  .card--slant .card__address { color: var(--ink); text-shadow: none; }
  .card--slant .card__email,
  .card--slant .card__phone { text-shadow: none; }
</style>
</head>
<body>

<svg width="0" height="0" style="position:absolute" aria-hidden="true">
  <defs>
    <linearGradient id="grass-fresh" x1="0" y1="0" x2="0" y2="1">
      <stop offset="0" stop-color="var(--grass-bright)"/>
      <stop offset="1" stop-color="var(--grass-mid)"/>
    </linearGradient>
    <linearGradient id="grass-dense" x1="0" y1="0" x2="1" y2="1">
      <stop offset="0" stop-color="#2f7a14"/>
      <stop offset="0.5" stop-color="var(--grass-mid)"/>
      <stop offset="1" stop-color="var(--grass-deep)"/>
    </linearGradient>
    <linearGradient id="grass-dew" x1="0" y1="0" x2="0" y2="1">
      <stop offset="0" stop-color="var(--grass-pale)"/>
      <stop offset="0.45" stop-color="var(--grass-bright)"/>
      <stop offset="1" stop-color="#74bd32"/>
    </linearGradient>
    <linearGradient id="sky" x1="0" y1="0" x2="0" y2="1">
      <stop offset="0" stop-color="var(--sky-top)"/>
      <stop offset="1" stop-color="var(--sky-low)"/>
    </linearGradient>
  </defs>
</svg>

<article class="card card--r1c1">
  <svg class="card__scene" viewBox="0 0 519 298">
    <path role="img" aria-label="Photo of fresh green lawn" d="M0 192 C120 184 250 206 350 214 C430 219 480 206 519 203 L519 298 L0 298 Z" fill="url(#grass-fresh)"/>
    <line x1="0" y1="258" x2="519" y2="258" stroke="#fff" stroke-width="1.5"/>
  </svg>
  <h2 class="card__name">Tobin Varemchuk</h2>
  <p class="card__title">National Sales Manager</p>
  <p class="card__brand">BRISK MEADOW</p>
  <p class="card__tagline">Premium Synthetic Turf</p>
  <p class="card__company">Brisk Meadow Inc.</p>
  <p class="card__address">1287 Harlow Ct Unit 9 Mississauga, Ontario L5T 2K6 Canada</p>
  <p class="card__email">tobin@briskmeadow.ca</p>
  <p class="card__phone">Call: 416-552-0918</p>
</article>

<article class="card card--r1c2">
  <svg class="card__scene" viewBox="0 0 519 298">
    <path role="img" aria-label="Photo of dense long green grass" d="M0 190 C120 184 250 206 350 214 C430 219 480 206 519 203 L519 298 L0 298 Z" fill="url(#grass-dense)"/>
    <line x1="0" y1="259" x2="519" y2="259" stroke="#fff" stroke-width="1.5"/>
  </svg>
  <h2 class="card__name">Tobin Varemchuk</h2>
  <p class="card__title">National Sales Manager</p>
  <p class="card__brand">BRISK MEADOW</p>
  <p class="card__tagline">Premium Synthetic Turf</p>
  <p class="card__company">Brisk Meadow Inc.</p>
  <p class="card__address">1287 Harlow Ct Unit 9 Mississauga, Ontario L5T 2K6 Canada</p>
  <p class="card__email">tobin@briskmeadow.ca</p>
  <p class="card__phone">Call: 416-552-0918</p>
</article>

<article class="card card--r2c1">
  <svg class="card__scene" viewBox="0 0 519 298">
    <rect role="img" aria-label="Close-up photo of dewy grass blades" x="0" y="157" width="519" height="141" fill="url(#grass-dew)"/>
    <line x1="0" y1="259" x2="519" y2="259" stroke="#fff" stroke-width="1.5"/>
  </svg>
  <h2 class="card__name">Tobin Varemchuk</h2>
  <p class="card__title">National Sales Manager</p>
  <p class="card__brand">BRISK MEADOW</p>
  <p class="card__tagline">Premium Synthetic Turf</p>
  <p class="card__company">Brisk Meadow Inc.</p>
  <p class="card__address">1287 Harlow Ct Unit 9 Mississauga, Ontario L5T 2K6 Canada</p>
  <p class="card__email">tobin@briskmeadow.ca</p>
  <p class="card__phone">Call: 416-552-0918</p>
</article>

<article class="card card--r2c2">
  <svg class="card__scene" viewBox="0 0 519 298">
    <path role="img" aria-label="Close-up photo of dewy grass blades" d="M0 208 C120 192 300 182 420 190 C470 194 500 198 519 200 L519 298 L0 298 Z" fill="url(#grass-dew)"/>
    <line x1="0" y1="259" x2="519" y2="259" stroke="#fff" stroke-width="1.5"/>
  </svg>
  <h2 class="card__name">Tobin Varemchuk</h2>
  <p class="card__title">National Sales Manager</p>
  <p class="card__brand">BRISK MEADOW</p>
  <p class="card__tagline">Premium Synthetic Turf</p>
  <p class="card__company">Brisk Meadow Inc.</p>
  <p class="card__address">1287 Harlow Ct Unit 9 Mississauga, Ontario L5T 2K6 Canada</p>
  <p class="card__email">tobin@briskmeadow.ca</p>
  <p class="card__phone">Call: 416-552-0918</p>
</article>

<article class="card card--r3c1 card--sky">
  <svg class="card__scene" viewBox="0 0 519 298">
    <rect role="img" aria-label="Photo of blue sky with soft clouds" x="0" y="0" width="519" height="182" fill="url(#sky)"/>
    <rect role="img" aria-label="Photo of open green field" x="0" y="182" width="519" height="116" fill="url(#grass-fresh)"/>
    <line x1="0" y1="259" x2="519" y2="259" stroke="#fff" stroke-width="1.5"/>
  </svg>
  <h2 class="card__name">Tobin Varemchuk</h2>
  <p class="card__title">National Sales Manager</p>
  <p class="card__brand">BRISK MEADOW</p>
  <p class="card__tagline">Premium Synthetic Turf</p>
  <p class="card__company">Brisk Meadow Inc.</p>
  <p class="card__address">1287 Harlow Ct Unit 9 Mississauga, Ontario L5T 2K6 Canada</p>
  <p class="card__email">tobin@briskmeadow.ca</p>
  <p class="card__phone">Call: 416-552-0918</p>
</article>

<article class="card card--r3c2 card--slant">
  <svg class="card__scene" viewBox="0 0 519 298">
    <polygon role="img" aria-label="Photo of fresh green lawn" points="0,66 519,200 519,258 0,258" fill="url(#grass-fresh)"/>
    <line x1="0" y1="64" x2="519" y2="198" stroke="var(--bar-black)" stroke-width="4"/>
    <rect x="0" y="258" width="519" height="40" fill="var(--bar-black)"/>
  </svg>
  <h2 class="card__name">Tobin Varemchuk</h2>
  <p class="card__title">National Sales Manager</p>
  <p class="card__brand">BRISK MEADOW</p>
  <p class="card__tagline">Premium Synthetic Turf</p>
  <p class="card__company">Brisk Meadow Inc.</p>
  <p class="card__address">1287 Harlow Ct Unit 9 Mississauga, Ontario L5T 2K6 Canada</p>
  <p class="card__email">tobin@briskmeadow.ca</p>
  <p class="card__phone">Call: 416-552-0918</p>
</article>

</body>
</html>
```